The Reefside Clinic PowerPoint Design

We are looking for a new PowerPoint template design to reflect our branding and to be used for presentations at international conferences and online conferences. An example of our current template which is outdated is attached. We would like to still have a blue colour background as this represents water (but the exact background can be modified). We would like a professional, modern, and sharp feel to the templates. The template should include an Intro Slide, content slide, and closing/questions slide. The template needs to be prepared for both the standards, the 4:3 and Wide screen 16:9. Logos and branding in the attached power point can be used. Please visit our website www.thereefsideclinic.com to see more about the company.

```html
<!DOCTYPE html>
<html lang="en">
<head>
<meta charset="utf-8">
<title>The Reefside Clinic – Presentation Template</title>
<link href="https://fonts.googleapis.com/css2?family=Open+Sans:wght@300;400;600;700&display=swap" rel="stylesheet">
<style>
:root{
  --navy:#1c3a78;
  --blue:#2f6fb5;
  --blue-mid:#3a86c8;
  --blue-light:#86b8e2;
  --blue-pale:#c9dcf0;
  --sky:#6ec0e8;
  --cyan:#2aa9dc;
  --ink:#24324a;
  --muted:#8a93a3;
  --green:#6db33f;
  --page:#ffffff;
}
*{box-sizing:border-box;margin:0;padding:0}
html,body{width:900px;height:1200px;overflow:hidden;background:var(--page)}
body{position:relative;font-family:"Open Sans",Arial,sans-serif;color:var(--ink)}
h1,h2,h3,h4{font-weight:400}
.slide{position:absolute;width:240px;height:180px;background:#fff;overflow:hidden;box-shadow:4px 6px 14px rgba(0,0,0,.28)}
.abs{position:absolute}
.brand{position:absolute;display:flex;align-items:center;gap:2px;font-size:4.6px;font-weight:600;color:var(--navy);white-space:nowrap}
.brand-dot{width:4px;height:4px;border-radius:50%;background:var(--cyan)}
.title{position:absolute;left:20px;font-size:9px;font-weight:400;color:var(--navy);letter-spacing:.2px;text-transform:uppercase;white-space:nowrap}
.subtitle{position:absolute;left:20px;font-size:2.2px;color:var(--muted);text-transform:uppercase;letter-spacing:.1px;white-space:nowrap}
.footer{position:absolute;left:17px;bottom:4px;font-size:3px;color:var(--muted)}
.page-no{position:absolute;right:17px;bottom:4px;font-size:3px;color:var(--muted)}
.photo{position:absolute}
.ph-sea{background:linear-gradient(160deg,#3aa3de,#0f5c9e)}
.ph-deep{background:linear-gradient(180deg,#2a8fd0,#0b4c8a)}
.ph-reef{background:linear-gradient(150deg,#5a6b8a,#2f6b4a 60%,#8c5a3a)}
.ph-fish{background:linear-gradient(135deg,#c9c0b0,#2d3fa8 55%,#e3d7a0)}
.ph-coral{background:linear-gradient(140deg,#d9a070,#8a2a1e 55%,#c98a4a)}
.ph-pale{background:linear-gradient(150deg,#d8dde0,#8fa2b0)}
.ph-shell{background:linear-gradient(120deg,#d8d0c4,#b8480c 50%,#3a2a1a)}
.ph-turtle{background:linear-gradient(160deg,#2a6b6a,#5a6a4a)}
.ph-bright{background:linear-gradient(170deg,#1aa0e0,#0a5aa8)}
.ph-penguin{background:linear-gradient(160deg,#7fc0c0,#2a3a3a 50%,#9ac070)}
.ph-jelly{background:linear-gradient(140deg,#1a4aa8,#e07a20 55%,#f0a040)}
.ph-seahorse{background:linear-gradient(140deg,#e0e0d8,#c08030 55%,#5a4a30)}
.ph-diver{background:linear-gradient(150deg,#2a3a5a,#4a6a8a)}
.ph-portrait{background:linear-gradient(160deg,#a8b8c8,#3a4a5a)}
.box{position:absolute;padding:6px 5px;color:#fff}
.box h4{font-size:3.6px;font-weight:400;margin-bottom:1.5px}
.box h4::after{content:"";display:block;width:6px;height:.4px;background:currentColor;margin-top:1.5px;opacity:.7}
.box p{font-size:2.6px;line-height:1.45}
.box p b{font-weight:700}
.box.dark{background:var(--blue)}
.box.mid{background:var(--blue-mid)}
.box.light{background:var(--blue-light)}
.box.sky{background:var(--sky)}
.box.pale{background:var(--blue-pale);color:var(--navy)}
.body-copy{position:absolute;font-size:2.6px;line-height:1.6;color:var(--ink)}
.body-copy b{color:var(--navy)}
.cover-title{position:absolute;left:0;right:0;top:127px;text-align:center;font-size:7.6px;font-weight:400;color:var(--navy)}
.cover-author{position:absolute;left:0;right:0;top:141px;text-align:center;font-size:3px;color:var(--navy)}
.cover-desc{position:absolute;left:22px;right:22px;top:154px;text-align:center;font-size:2.6px;line-height:1.5;color:var(--navy)}
.partner-badge{position:absolute;left:196px;top:104px;width:40px;height:14px;background:var(--green)}
.team-card{position:absolute;height:48px;color:#fff;padding:7px 5px 0}
.team-card .name{font-size:3.6px;margin-bottom:1px}
.team-card .cred{font-size:2.1px;opacity:.85;margin-bottom:2px}
.team-card .bio{font-size:2.4px;line-height:1.45}
.vision-tile{position:absolute;width:92px;height:49px;background:var(--blue);border-radius:0 0 16px 0;overflow:hidden}
.vision-tile .photo{left:0;top:0;width:39px;height:49px}
.vision-tile .copy{position:absolute;left:44px;top:10px;right:6px;color:#fff}
.vision-tile h4{font-size:3.8px;font-weight:400;margin-bottom:2px}
.vision-tile p{font-size:2.5px;line-height:1.5}
.stack-title{position:absolute;left:19px;top:58px;font-size:11px;line-height:.95;color:var(--navy);font-weight:400}
.rule{position:absolute;height:.8px;background:var(--navy)}
.closing-title{position:absolute;left:17px;top:62px;font-size:15px;font-weight:400;color:var(--navy)}
.closing-note{position:absolute;left:17px;top:85px;width:100px;font-size:2.4px;line-height:1.5;color:var(--muted)}
</style>
</head>
<body>

<section class="slide" style="left:144px;top:13px">
  <div class="brand" style="right:8px;top:8px"><span class="brand-dot"></span>The Reefside Clinic</div>
  <div class="photo ph-fish" style="left:0;top:23px;width:240px;height:89px" role="img" aria-label="Clown triggerfish swimming in an aquarium"></div>
  <div class="partner-badge"></div>
  <h1 class="cover-title">Module One - Fish Anatomy and Physiology</h1>
  <p class="cover-author">Dr Sam Hollis</p>
  <p class="cover-desc">Examines teleost anatomy in its wide forms as well as practical physiology. To understand how fish survive in an aquatic environment is critical to maintaining their health and wellbeing. Normal anatomy is critical for diagnostics and post-mortems</p>
  <p class="footer">The Reefside Clinic presentation to:</p><p class="page-no">Page: 1</p>
</section>

<section class="slide" style="left:510px;top:13px">
  <h2 class="title" style="top:20px">Our Team</h2>
  <p class="subtitle" style="top:36px">Short line of supporting detail for this slide</p>
  <div class="brand" style="right:20px;top:24px"><span class="brand-dot"></span>The Reefside Clinic</div>
  <div class="photo ph-diver" style="left:18px;top:52px;width:36px;height:48px" role="img" aria-label="Team member portrait in diving suit"></div>
  <div class="team-card" style="left:54px;top:52px;width:66px;background:var(--blue)">
    <p class="name">Dr Sam Hollis</p><p class="cred">Veterinary degree, aquatic health</p>
    <p class="bio"><b>Lorem Ipsum</b> brief profile text about this team member and role.</p>
  </div>
  <div class="photo ph-turtle" style="left:120px;top:52px;width:36px;height:48px" role="img" aria-label="Team member portrait with sea turtle"></div>
  <div class="team-card" style="left:156px;top:52px;width:65px;background:var(--blue)">
    <p class="name">Dr Neil Varga</p><p class="cred">Bachelor of science in biology</p>
    <p class="bio"><b>Lorem Ipsum</b> brief profile text about this team member and role.</p>
  </div>
  <div class="team-card" style="left:18px;top:105px;width:66px;background:var(--blue-light)">
    <p class="name">Dr Owen Pratt</p><p class="cred">Marine biology degree</p>
    <p class="bio"><b>Lorem Ipsum</b> brief profile text about this team member and role.</p>
  </div>
  <div class="photo ph-portrait" style="left:84px;top:105px;width:36px;height:48px" role="img" aria-label="Team member portrait"></div>
  <div class="team-card" style="left:120px;top:105px;width:66px;background:var(--blue-light)">
    <p class="name">Dr. Leo Castell</p><p class="cred">Bachelor of science, first class</p>
    <p class="bio"><b>Lorem Ipsum</b> brief profile text about this team member and role.</p>
  </div>
  <div class="photo ph-portrait" style="left:186px;top:105px;width:35px;height:48px" role="img" aria-label="Team member portrait with dog"></div>
  <p class="footer">The Reefside Clinic presentation to:</p><p class="page-no">Page: 2</p>
</section>

<section class="slide" style="left:144px;top:212px">
  <h2 class="title" style="top:20px">Our Vision</h2>
  <p class="subtitle" style="top:36px">To advance the health and welfare of aquatic animals in aquariums and zoos globally</p>
  <div class="brand" style="right:20px;top:24px"><span class="brand-dot"></span>The Reefside Clinic</div>
  <div class="vision-tile" style="left:24px;top:52px"><div class="photo ph-penguin" role="img" aria-label="Penguin swimming underwater"></div><div class="copy"><h4>Consultation</h4><p><b>Lorem Ipsum</b> short note describing this service area.</p></div></div>
  <div class="vision-tile" style="left:122px;top:52px"><div class="photo ph-seahorse" role="img" aria-label="Seahorse"></div><div class="copy"><h4>Education</h4><p><b>Lorem Ipsum</b> short note describing this service area.</p></div></div>
  <div class="vision-tile" style="left:24px;top:106px"><div class="photo ph-fish" role="img" aria-label="Clown triggerfish"></div><div class="copy"><h4>Conferences</h4><p><b>Lorem Ipsum</b> short note describing this service area.</p></div></div>
  <div class="vision-tile" style="left:122px;top:106px"><div class="photo ph-jelly" role="img" aria-label="Jellyfish"></div><div class="copy"><h4>Reproduction</h4><p><b>Lorem Ipsum</b> short note describing this service area.</p></div></div>
  <p class="footer">The Reefside Clinic presentation to:</p><p class="page-no">Page: 3</p>
</section>

<section class="slide" style="left:510px;top:212px">
  <h2 class="title" style="top:20px">Content Slide</h2>
  <p class="subtitle" style="top:36px">Short line of supporting detail for this slide</p>
  <div class="brand" style="right:20px;top:24px"><span class="brand-dot"></span>The Reefside Clinic</div>
  <p class="footer">The Reefside Clinic presentation to:</p><p class="page-no">Page: 4</p>
</section>

<section class="slide" style="left:144px;top:411px">
  <div class="brand" style="left:20px;top:26px"><span class="brand-dot"></span>The Reefside Clinic</div>
  <h2 class="title" style="top:50px">Text With Image</h2>
  <p class="subtitle" style="top:66px">Short line of supporting detail</p>
  <p class="body-copy" style="left:18px;top:81px;width:100px"><b>Lorem Ipsum</b> body copy introducing the topic sits here, set in short lines beside the picture so the idea reads quickly and clearly for the audience in the room.<br><br>A second paragraph adds supporting detail in the same style, giving the presenter space for context, key findings and a closing point.</p>
  <div class="photo ph-shell" style="left:133px;top:0;width:107px;height:180px" role="img" aria-label="Backlit shark egg case held in a hand"></div>
  <p class="footer">The Reefside Clinic presentation to:</p>
</section>

<section class="slide" style="left:510px;top:411px">
  <h2 class="title" style="top:20px">Portfolio Options</h2>
  <p class="subtitle" style="top:36px">Short line of supporting detail for this slide</p>
  <div class="brand" style="right:20px;top:24px"><span class="brand-dot"></span>The Reefside Clinic</div>
  <div class="photo ph-reef" style="left:18px;top:48px;width:55px;height:105px" role="img" aria-label="Discus fish among aquarium plants"></div>
  <div class="photo ph-deep" style="left:74px;top:48px;width:54px;height:54px" role="img" aria-label="Shark in blue water"></div>
  <div class="box dark" style="left:74px;top:103px;width:54px;height:50px;padding:3px 4px"><h4>Content Text here</h4><p><b>Lorem Ipsum</b> short caption text for this image group.</p></div>
  <div class="photo ph-sea" style="left:129px;top:48px;width:92px;height:54px" role="img" aria-label="Spotted eagle ray"></div>
  <div class="photo ph-pale" style="left:129px;top:103px;width:92px;height:50px" role="img" aria-label="Close view of a zebra shark"></div>
  <p class="footer">The Reefside Clinic presentation to:</p><p class="page-no">Page: 6</p>
</section>

<section class="slide" style="left:144px;top:610px">
  <h2 class="title" style="top:20px">Portfolio Options</h2>
  <p class="subtitle" style="top:36px">Short line of supporting detail for this slide</p>
  <div class="brand" style="right:20px;top:24px"><span class="brand-dot"></span>The Reefside Clinic</div>
  <div class="photo ph-fish" style="left:0;top:52px;width:40px;height:53px" role="img" aria-label="Clown triggerfish"></div>
  <div class="box dark" style="left:40px;top:52px;width:40px;height:53px"><h4>Content Text</h4><p><b>Lorem Ipsum</b> short caption for this image.</p></div>
  <div class="photo ph-reef" style="left:80px;top:52px;width:40px;height:53px" role="img" aria-label="Discus fish among plants"></div>
  <div class="box pale" style="left:120px;top:52px;width:40px;height:53px"><h4>Content Text</h4><p><b>Lorem Ipsum</b> short caption for this image.</p></div>
  <div class="photo ph-deep" style="left:160px;top:52px;width:40px;height:53px" role="img" aria-label="Shark in blue water"></div>
  <div class="box mid" style="left:200px;top:52px;width:40px;height:53px"><h4>Content Text</h4><p><b>Lorem Ipsum</b> short caption for this image.</p></div>
  <div class="box dark" style="left:0;top:105px;width:40px;height:52px"><h4>Content Text</h4><p><b>Lorem Ipsum</b> short caption for this image.</p></div>
  <div class="photo ph-coral" style="left:40px;top:105px;width:40px;height:52px" role="img" aria-label="Red frogfish on sand"></div>
  <div class="box light" style="left:80px;top:105px;width:40px;height:52px"><h4>Content Text</h4><p><b>Lorem Ipsum</b> short caption for this image.</p></div>
  <div class="photo ph-bright" style="left:120px;top:105px;width:40px;height:52px" role="img" aria-label="Sea turtle swimming"></div>
  <div class="box sky" style="left:160px;top:105px;width:40px;height:52px"><h4>Content Text</h4><p><b>Lorem Ipsum</b> short caption for this image.</p></div>
  <div class="photo ph-bright" style="left:200px;top:105px;width:40px;height:52px" role="img" aria-label="Reef with schooling fish"></div>
  <p class="footer">The Reefside Clinic presentation to:</p><p class="page-no">Page: 7</p>
</section>

<section class="slide" style="left:510px;top:610px">
  <h2 class="title" style="top:20px">Portfolio Options</h2>
  <p class="subtitle" style="top:36px">Short line of supporting detail for this slide</p>
  <div class="brand" style="right:20px;top:24px"><span class="brand-dot"></span>The Reefside Clinic</div>
  <div class="photo ph-deep" style="left:0;top:52px;width:120px;height:105px" role="img" aria-label="Sand tiger shark in blue water"></div>
  <div class="box pale" style="left:120px;top:52px;width:40px;height:53px"><h4>Text</h4><p><b>Lorem Ipsum</b> short caption for this image.</p></div>
  <div class="photo ph-sea" style="left:120px;top:105px;width:40px;height:52px" role="img" aria-label="Spotted eagle ray"></div>
  <div class="photo ph-pale" style="left:160px;top:52px;width:40px;height:53px" role="img" aria-label="Zebra shark close up"></div>
  <div class="box light" style="left:160px;top:105px;width:40px;height:52px;padding-top:2px"><h4>Text</h4><p><b>Lorem Ipsum</b> short caption for this image.</p></div>
  <div class="box mid" style="left:200px;top:52px;width:40px;height:53px"><h4>Text</h4><p><b>Lorem Ipsum</b> short caption for this image.</p></div>
  <div class="photo ph-coral" style="left:200px;top:105px;width:40px;height:52px" role="img" aria-label="Red frogfish"></div>
  <p class="footer">The Reefside Clinic presentation to:</p><p class="page-no">Page: 8</p>
</section>

<section class="slide" style="left:144px;top:808px">
  <h2 class="title" style="top:20px">Text With Two Images</h2>
  <p class="subtitle" style="top:36px">Short line of supporting detail for this slide</p>
  <div class="brand" style="right:20px;top:24px"><span class="brand-dot"></span>The Reefside Clinic</div>
  <div class="photo ph-deep" style="left:18px;top:47px;width:98px;height:85px" role="img" aria-label="Shark swimming in blue water"></div>
  <div class="photo ph-pale" style="left:124px;top:47px;width:98px;height:85px" role="img" aria-label="Zebra shark close up"></div>
  <p class="body-copy" style="left:18px;top:136px;width:98px"><b>Lorem Ipsum</b> caption text describing the image above, written across two short lines.</p>
  <p class="body-copy" style="left:124px;top:136px;width:98px"><b>Lorem Ipsum</b> caption text describing the image above, written across two short lines.</p>
  <p class="footer">The Reefside Clinic presentation to:</p><p class="page-no">Page: 9</p>
</section>

<section class="slide" style="left:510px;top:808px">
  <h2 class="title" style="top:20px">Portfolio Images</h2>
  <p class="subtitle" style="top:36px">Short line of supporting detail for this slide</p>
  <div class="brand" style="right:20px;top:24px"><span class="brand-dot"></span>The Reefside Clinic</div>
  <div class="photo ph-fish" style="left:18px;top:48px;width:74px;height:55px" role="img" aria-label="Clown triggerfish"></div>
  <div class="photo ph-reef" style="left:93px;top:48px;width:55px;height:55px" role="img" aria-label="Discus fish among plants"></div>
  <div class="photo ph-sea" style="left:149px;top:48px;width:72px;height:55px" role="img" aria-label="Spotted eagle ray"></div>
  <div class="photo ph-coral" style="left:18px;top:104px;width:52px;height:49px" role="img" aria-label="Red frogfish"></div>
  <div class="photo ph-bright" style="left:71px;top:104px;width:94px;height:49px" role="img" aria-label="Sea turtle over reef"></div>
  <div class="photo ph-turtle" style="left:166px;top:104px;width:55px;height:49px" role="img" aria-label="Turtle resting on reef"></div>
  <p class="footer">The Reefside Clinic presentation to:</p><p class="page-no">Page: 10</p>
</section>

<section class="slide" style="left:144px;top:1007px">
  <div class="brand" style="left:20px;top:26px"><span class="brand-dot"></span>The Reefside Clinic</div>
  <h2 class="stack-title">TEXT WITH<br>FOUR<br>IMAGES</h2>
  <p class="body-copy" style="left:19px;top:96px;width:82px"><b>Lorem Ipsum</b> body copy introducing the topic with four supporting images beside it, giving the audience clear context at a glance.</p>
  <div class="photo ph-penguin" style="left:106px;top:22px;width:51px;height:101px" role="img" aria-label="Penguin swimming underwater"></div>
  <div class="photo ph-turtle" style="left:158px;top:22px;width:50px;height:44px" role="img" aria-label="Turtle on reef"></div>
  <div class="photo ph-bright" style="left:158px;top:68px;width:50px;height:89px" role="img" aria-label="Reef with schooling fish"></div>
  <div class="photo ph-fish" style="left:106px;top:125px;width:51px;height:32px" role="img" aria-label="Clown triggerfish"></div>
  <div class="rule" style="left:158px;top:66px;width:78px"></div>
  <div class="rule" style="left:0;top:124px;width:106px"></div>
  <p class="footer">The Reefside Clinic presentation to:</p><p class="page-no">Page: 11</p>
</section>

<section class="slide" style="left:510px;top:1007px">
  <div class="brand" style="left:20px;top:26px"><span class="brand-dot"></span>The Reefside Clinic</div>
  <svg class="abs" style="left:0;top:0" width="240" height="180" viewBox="0 0 240 180" aria-hidden="true">
    <polygon points="76,178 86,178 200,0 190,0" fill="#1f6fc0"/>
    <polygon points="90,150 98,150 190,8 182,8" fill="#3a9be0"/>
    <polygon points="104,162 112,162 214,0 206,0" fill="#2a85d0"/>
    <polygon points="118,140 126,140 216,4 208,4" fill="#86b8e2"/>
    <polygon points="112,180 122,180 228,10 218,10" fill="#1aa0e0"/>
    <polygon points="134,158 142,158 230,20 222,20" fill="#5aa6dc"/>
    <polygon points="150,110 156,110 222,8 216,8" fill="#2f6fb5"/>
  </svg>
  <h2 class="closing-title">QUESTIONS?</h2>
  <p class="closing-note">Closing remarks and contact details for questions go here, set over two short lines.</p>
</section>

</body>
</html>
```